Pelmar Grove에서 세계시장을 겨냥한 신제품 프리미엄 코르닉 스마트 체중계 출시에 맞춰 사용자 편의 위주의 가독성있는 반응형 앱의 UI UX디자인을 공모합니다. 앱의 주요 타겟층은 세계 20-40대 여성분들입니다. 향후 다양한 언어로 출시 예정이니 직관적, 전문적, 심플함위주의 가시성있는 그래픽을 선호하며 유저중심의 UI UX를 추구합니다.

```html
<!DOCTYPE html>
<html lang="ko">
<head>
<meta charset="utf-8">
<title>Pelmar Grove Health Fit — Welcome</title>
<link rel="stylesheet" href="https://fonts.googleapis.com/css2?family=Montserrat:wght@600;800;900&family=Noto+Sans+KR:wght@500;700&display=swap">
<style>
  :root {
    --page-bg: #f2f2f2;
    --screen-bg: #ffffff;
    --hero-dark: #161616;
    --hero-mid: #2b2624;
    --hero-warm: #4a3a33;
    --brand-orange: #f15a29;
    --ink-dark: #1f1f1f;
    --text-light: #ffffff;
    --product-white: #f7f7f7;
    --product-shade: #e4e4e4;
  }
  * { box-sizing: border-box; margin: 0; padding: 0; }
  html, body {
    width: 1200px;
    height: 1200px;
    overflow: hidden;
    background: var(--page-bg);
  }
  .canvas {
    width: 1200px;
    height: 1200px;
    display: flex;
    align-items: center;
    justify-content: center;
  }
  .app-screen {
    position: relative;
    width: 540px;
    height: 1110px;
    background: var(--screen-bg);
    border-radius: 36px;
    overflow: hidden;
    box-shadow: 0 20px 60px rgba(0,0,0,0.12);
  }
  .hero {
    position: absolute;
    inset: 0 0 auto 0;
    height: 700px;
    background:
      linear-gradient(180deg, rgba(22,22,22,0.92) 0%, rgba(22,22,22,0.55) 45%, rgba(22,22,22,0.85) 100%),
      linear-gradient(160deg, var(--hero-mid) 0%, var(--hero-warm) 55%, var(--hero-dark) 100%);
  }
  .hero-content {
    position: absolute;
    top: 210px;
    left: 0;
    right: 0;
    text-align: center;
    color: var(--text-light);
  }
  .brand-mark {
    display: inline-flex;
    align-items: center;
    gap: 8px;
    font-family: "Montserrat", sans-serif;
    font-weight: 800;
    font-size: 15px;
    letter-spacing: 1px;
    color: var(--text-light);
    margin-bottom: 26px;
  }
  .brand-mark .dot {
    width: 14px;
    height: 14px;
    border-radius: 50%;
    background: var(--text-light);
  }
  .headline {
    font-family: "Montserrat", sans-serif;
    font-weight: 900;
    font-size: 44px;
    line-height: 1.05;
    letter-spacing: 0.5px;
    text-transform: uppercase;
  }
  .product {
    position: absolute;
    top: 560px;
    left: 50%;
    transform: translateX(-50%);
    width: 300px;
    height: 300px;
    border-radius: 44px;
    background: linear-gradient(145deg, var(--product-white) 0%, var(--product-shade) 100%);
    box-shadow: 0 24px 40px rgba(0,0,0,0.18);
  }
  .actions {
    position: absolute;
    left: 32px;
    right: 32px;
    bottom: 60px;
    display: flex;
    flex-direction: column;
    gap: 16px;
  }
  .btn {
    height: 64px;
    border-radius: 32px;
    display: flex;
    align-items: center;
    justify-content: center;
    font-family: "Noto Sans KR", sans-serif;
    font-weight: 700;
    font-size: 19px;
    color: var(--text-light);
  }
  .btn-signup { background: var(--brand-orange); }
  .btn-login { background: var(--ink-dark); }
</style>
</head>
<body>
  <main class="canvas">
    <section class="app-screen">
      <div class="hero" role="img" aria-label="Dark gym photo of a woman training, used as welcome background"></div>
      <div class="hero-content">
        <div class="brand-mark"><span class="dot"></span>Pelmar Grove</div>
        <h1 class="headline">Welcome<br>Pelmar Grove<br>Health Fit</h1>
      </div>
      <div class="product" role="img" aria-label="Product photo of the white Kornik smart body scale"></div>
      <div class="actions">
        <div class="btn btn-signup">회원가입</div>
        <div class="btn btn-login">로그인</div>
      </div>
    </section>
  </main>
</body>
</html>
```